Halvard Atelier Business cards

Design our business cards and eventually a logo. The company is based in Paris, its activity is the retailing via internet of luxury home furniture (like Vambrelli, Bercusa, tarvoni...) Our clients are international andwith a high sense of aesthetics. The design shall communicate wealth and trust with a high quality and aesthetic sense, pure lines Company Name is Halvard AtelierExplanation of the name: usually people who wants to buy furniture usually go in a showroom. Today they go in showroom to test the furniture and they search for the price on internet, which is a "Halvard atelier".We will not be a e-commerce site. Our site will be (another project) a presentation site which purpose is to reach qualified prospects. Then everything will be handled by phone, meeting etc.The business card must be professional as we will negotiate with many luxury brands, opportunity to represent them on our site, prices etc.As far as the color are concerned mostly black and whithe or grey. The font of the Halvard Atelier name shall have some impact.

Target Market(s)

High-end furniture and buyers of luxury goods, international customers, mostly women who handle such projects.
We also deal with professional buyers (hotels as an example) and luxury brands

Contact Information for Business Card

standard format 85x55, lanscape card, square corners will be printed on thick high quality paper (300 or 350g)

Font styles to use
Sans Serif

Colors

Designer to choose colors to be used in the design.

Requirements
Must have
• Must be white, as the paper will be high quality, the paper will enhance the card.
• Name of the brand Halvard atelier (with specific font which make it very nice looking and catch the attention. similar to Calibri or Calibri
• Name of person (will give you the name later (4 names and position)
• the position of the person
• Mobile phone, e-mail, Physical address 27, rue Fenouillard, 75005 Paris, France (courrier only) our web site www.halvardatelier.fr
• The card must be simple and class
Nice to have
• Font of the address is smaller than the rest,
• Calibri font or similar on recto side with the name of the company which may look similar to the picture inserted in the brief.
• The grey color in the picture inserted is ok for us
Should not have
• Any parallel lines which represent the name of the company
• Any heavy design If you go on internet sites which present the furniture all designs are pure lines and high quality craftsmanship. To have an idea of our targetted client or brand we will be in touch: https://www.casavelumi.it/projects/
• Note that the picture added below is what we use, now as mail signature, up to you to have a better design etc.

```html
<!DOCTYPE html>
<html lang="en">
<head>
<meta charset="utf-8">
<title>Halvard Atelier – Business Cards</title>
<link href="https://fonts.googleapis.com/css2?family=Carlito:wght@400;700&display=swap" rel="stylesheet">
<style>
  :root {
    --backdrop: #151515;
    --card: #1d1d1d;
    --card-edge: #262626;
    --ink: #f4f4f4;
    --gloss: #7c7c7c;
    --rule: #e6e6e6;
  }
  * { margin: 0; padding: 0; box-sizing: border-box; }
  html, body {
    width: 1200px;
    height: 900px;
    overflow: hidden;
    background: var(--backdrop);
    font-family: "Carlito", "Calibri", sans-serif;
  }
  .sheet {
    width: 1200px;
    height: 900px;
    display: flex;
    flex-direction: column;
    align-items: center;
    justify-content: center;
    gap: 36px;
  }
  .card {
    width: 600px;
    height: 388px;
    background: var(--card);
    border: 1px solid var(--card-edge);
    position: relative;
    color: var(--ink);
  }
  .card--front {
    display: flex;
    align-items: center;
    justify-content: center;
  }
  .front-name {
    font-size: 30px;
    font-weight: 700;
    letter-spacing: 2px;
    text-transform: uppercase;
    color: var(--gloss);
    margin-top: -20px;
  }
  .card--back {
    display: flex;
    align-items: center;
    padding-left: 62px;
  }
  .back-name {
    font-size: 31px;
    font-weight: 700;
    width: 270px;
    margin-top: -62px;
  }
  .divider {
    width: 2px;
    height: 150px;
    background: var(--rule);
    margin: 0 34px 0 12px;
  }
  .contact { line-height: 1.2; }
  .contact__person { font-size: 23px; }
  .contact__role { font-size: 17px; margin-bottom: 10px; }
  .contact__line { font-size: 18px; }
</style>
</head>
<body>
  <main class="sheet">
    <section class="card card--front" aria-label="Card front">
      <h1 class="front-name">Halvard Atelier SAS</h1>
    </section>
    <section class="card card--back" aria-label="Card back">
      <h2 class="back-name">Halvard Atelier SAS</h2>
      <div class="divider"></div>
      <address class="contact" style="font-style:normal">
        <p class="contact__person">Mathis Corvenne</p>
        <p class="contact__role">President / Co-Founder</p>
        <p class="contact__line">+33641907218</p>
        <p class="contact__line">27 rue Fenouillard</p>
        <p class="contact__line">75005 Paris, France</p>
        <p class="contact__line">www.halvardatelier.fr</p>
      </address>
    </section>
  </main>
</body>
</html>
```